An international wholesale business needs letterhead design

Logo file is attached. Please design a letterhead with the following details:

- Company Name and Logo
- Address
- VAT Registration number
- Phone No
- Website address

```html
<!DOCTYPE html>
<html lang="en">
<head>
<meta charset="utf-8">
<title>Korvell Trading Letterhead</title>
<link rel="stylesheet" href="https://fonts.googleapis.com/css2?family=Open+Sans:wght@400;600&family=Lato:wght@400;700&display=swap">
<style>
  :root {
    --backdrop: #dbdee6;
    --paper: #ffffff;
    --brand-red: #c1272d;
    --body-text: #555555;
    --footer-text: #222222;
    --rule: #d5d5d5;
    --signature-tone: #e6e6e6;
  }
  html, body {
    margin: 0;
    padding: 0;
    width: 1062px;
    height: 1200px;
    overflow: hidden;
    background: var(--backdrop);
  }
  .letterhead {
    position: absolute;
    left: 234px;
    top: 260px;
    width: 595px;
    height: 767px;
    background: var(--paper);
    font-family: "Open Sans", sans-serif;
    color: var(--body-text);
  }
  .brand {
    position: absolute;
    left: 0;
    top: 24px;
    width: 100%;
    display: flex;
    justify-content: center;
    align-items: center;
    gap: 10px;
  }
  .brand-mark {
    width: 30px;
    height: 30px;
    border-radius: 50%;
    background: var(--brand-red);
  }
  .brand-name {
    font-weight: 600;
    font-size: 24px;
    letter-spacing: 1px;
    color: var(--brand-red);
  }
  .letter-body {
    position: absolute;
    left: 56px;
    top: 150px;
    width: 481px;
    font-size: 9.4px;
  }
  .letter-body p { margin: 0; }
  .issue-date { margin-bottom: 12px !important; }
  .recipient { line-height: 11.7px; margin-bottom: 33px !important; }
  .salutation { margin-bottom: 17px !important; }
  .paragraph {
    line-height: 17.2px;
    text-align: justify;
    margin-bottom: 17px !important;
    hyphens: auto;
    -webkit-hyphens: auto;
  }
  .closing { margin-top: 34px !important; }
  .signature {
    display: block;
    width: 136px;
    height: 14px;
    margin: 14px 0 10px;
    background: linear-gradient(90deg, var(--signature-tone), #f3f3f3);
  }
  .signer-name {
    font-size: 12px;
    font-weight: 600;
    color: #4a4a4a;
  }
  .signer-title { margin-top: 4px !important; }
  .footer {
    position: absolute;
    left: 0;
    top: 722px;
    width: 100%;
    font-family: "Lato", sans-serif;
    color: var(--footer-text);
    text-align: center;
  }
  .footer-address { font-size: 11.6px; margin: 0; }
  .footer-rule {
    width: 410px;
    height: 1px;
    background: var(--rule);
    margin: 4px auto 3px;
  }
  .footer-contacts { font-size: 11.6px; margin: 0; }
  .label { color: var(--brand-red); font-weight: 700; }
  .label-vat { color: var(--brand-red); }
</style>
</head>
<body>
  <main class="letterhead">
    <header class="brand">
      <span class="brand-mark"></span>
      <span class="brand-name">KORVELL TRADING</span>
    </header>

    <section class="letter-body">
      <p class="issue-date">Issuing Date: May 5, 2018</p>
      <p class="recipient">Name Of Employee Mr. XYZABC<br>Address of Employee<br>Address Line 2 etc..</p>
      <p class="salutation">Dear Mr.XYZABC</p>
      <p class="paragraph">Lorem Ipsum has been the industry's standard dummy text ever since the 1500s, when an unknown printer took a galley of type and scrambled it to make a type specimen book. It has survived not only five centuries, but also the leap into electronic typesetting, remaining essentially unchanged. It was popularised in the 1960s with the release of Letraset sheets containing Lorem Ipsum passages, and more recently with desktop publishing software like Aldus PageMaker including versions of Lorem Ipsum.</p>
      <p class="paragraph">Lorem Ipsum is simply dummy text of the printing and typesetting industry. Lorem Ipsum has been the industry's standard dummy text ever since the 1500s, when an unknown printer took a galley of type and scrambled it to make a type specimen book.</p>
      <p class="paragraph">It has survived not only five centuries, but also the leap into electronic typesetting, remaining essentially unchanged. It was popularised in the 1960s with the release of Letraset sheets containing Lorem IpsumIpsum passages.</p>
      <p class="closing">Yours Sincerely</p>
      <span class="signature" role="img" aria-label="Handwritten signature of Marcus Hale"></span>
      <p class="signer-name">Marcus Hale</p>
      <p class="signer-title">Managing Director</p>
    </section>

    <footer class="footer">
      <p class="footer-address">78, Harbour Road Westvale Country, 30918</p>
      <div class="footer-rule"></div>
      <p class="footer-contacts"><span class="label">P:</span> 021-555 310 642 &nbsp;| <span class="label">W:</span> www.korvelltrade.com | &nbsp;<span class="label-vat">VAT Registration No:</span>&nbsp; 7741209</p>
    </footer>
  </main>
</body>
</html>
```